Design home page for SME Brightfold

WordPress homepage for SME Brightfold.
Will use GeneratePress, and the theme will be a child theme of Generate Press.
Logo attached.
SME Brightfold is a business that advises Small to Medium Businesses towards success.

```html
<!DOCTYPE html>
<html lang="en">
<head>
<meta charset="utf-8">
<title>SME Brightfold – Home</title>
<link href="https://fonts.googleapis.com/css2?family=Josefin+Sans:wght@400;600;700&family=Mulish:wght@400;600;700;800&display=swap" rel="stylesheet">
<style>
:root{
  --slate:#7a8899;
  --slate-dark:#66768a;
  --ink:#1f1f1f;
  --text:#333;
  --muted:#555;
  --soft:#f3f2f2;
  --white:#fff;
  --footer:#1d1d1d;
}
*{box-sizing:border-box;margin:0;padding:0}
html,body{width:1200px;height:3795px;overflow:hidden}
body{position:relative;background:var(--white);font-family:'Mulish',sans-serif;color:var(--text)}
.abs{position:absolute}
.btn{position:absolute;display:flex;align-items:center;justify-content:center;background:var(--slate);color:var(--white);font-family:'Josefin Sans',sans-serif;font-weight:700;letter-spacing:.3px;border-radius:6px;text-decoration:none}
.rule{position:absolute;height:3px;width:32px;background:var(--slate)}
.photo{position:absolute}

/* header */
.brand{position:absolute;display:flex;align-items:center;gap:10px;font-family:'Josefin Sans',sans-serif;font-weight:600;color:var(--slate-dark);white-space:nowrap}
.brand .dot{border-radius:50%;background:var(--slate-dark)}
.site-header .brand{left:132px;top:32px;font-size:28px}
.site-header .brand .dot{width:30px;height:30px}
.follow{left:710px;top:28px;font-size:10px;display:flex;align-items:center;gap:10px;color:var(--ink)}
.follow i{display:inline-block;width:12px;height:12px;border-radius:50%;background:var(--slate)}
.call{left:893px;top:17px;display:flex;gap:10px;align-items:center}
.call .ico{width:26px;height:26px;border-radius:50%;background:var(--slate);display:flex;align-items:center;justify-content:center}
.call small{display:block;font-size:12px;color:var(--ink)}
.call strong{font-size:17px;font-weight:400;color:var(--ink)}
.nav{left:616px;top:68px;display:flex;gap:38px;font-size:14px;color:var(--ink);font-family:'Josefin Sans',sans-serif}
.nav .active{color:var(--slate);font-weight:700}

/* hero */
.hero h1{position:absolute;left:130px;top:146px;font-family:'Josefin Sans',sans-serif;font-weight:600;font-size:35px;line-height:40px;letter-spacing:1.5px;color:var(--ink)}
.hero h1 span{color:var(--slate)}
.hero p{position:absolute;left:132px;top:240px;width:380px;font-size:14px;line-height:20px;color:var(--ink)}
.diamond{position:absolute;transform:rotate(45deg);border-radius:26px;overflow:hidden}

/* services */
.band-soft{position:absolute;left:0;width:1200px;background:var(--soft)}
.sec-title{position:absolute;left:0;width:1200px;text-align:center;font-family:'Josefin Sans',sans-serif;font-weight:600;font-size:24px;letter-spacing:1.5px;color:var(--ink)}
.sec-title span{color:var(--slate)}
.service{position:absolute;top:717px;width:224px;height:293px;background:var(--white);border-radius:8px;text-align:center;box-shadow:0 2px 8px rgba(0,0,0,.04)}
.service svg{margin-top:24px}
.service h3{margin:18px auto 0;width:150px;font-family:'Josefin Sans',sans-serif;font-weight:600;font-size:15px;line-height:19px;letter-spacing:1px;color:var(--slate)}
.service p{margin:16px auto 0;width:185px;font-size:11.5px;line-height:15.5px;color:var(--muted)}
.service .btn{left:64px;top:233px;width:96px;height:29px;font-size:11px;border-radius:4px}
.service.featured{background:var(--slate)}
.service.featured h3,.service.featured p{color:var(--white)}
.service.featured .btn{background:var(--white);color:var(--slate)}

/* welcome */
.welcome h2,.skills h2{position:absolute;font-family:'Josefin Sans',sans-serif;font-weight:600;letter-spacing:1.5px;color:var(--ink)}
.welcome h2{left:642px;top:1130px;font-size:24px;line-height:34px}
.welcome h2 span{font-size:30px;color:var(--slate)}
.lead{position:absolute;left:644px;top:1236px;width:380px;font-weight:800;font-size:14px;line-height:22px;color:var(--slate)}
.body-copy{position:absolute;font-size:14.5px;line-height:20.2px;color:var(--ink)}

/* why */
.why{position:absolute;left:0;top:1605px;width:1200px;height:450px;background:var(--slate)}
.why-title{position:absolute;left:0;top:50px;width:1200px;text-align:center;color:var(--white);font-family:'Josefin Sans',sans-serif;font-size:23px;letter-spacing:1.5px}
.why .rule{background:var(--white);left:584px;top:88px}
.reason{position:absolute;top:145px;width:280px;text-align:center;color:var(--white)}
.reason h3{margin-top:22px;font-family:'Josefin Sans',sans-serif;font-weight:600;font-size:18px;letter-spacing:.8px}
.reason p{margin-top:14px;font-size:11.5px;line-height:16px}

/* skills */
.skills h2{left:130px;top:2135px;font-size:30px;line-height:38px}
.skills h2 span{color:var(--slate)}

/* blog */
.post{position:absolute;top:2742px;width:300px;height:362px;background:var(--white);border-radius:8px;overflow:hidden}
.post .photo{position:static;display:block;width:300px;height:177px}
.post h3{margin:22px 28px 0;font-family:'Josefin Sans',sans-serif;font-weight:600;font-size:16.5px;line-height:20px;letter-spacing:1px;color:var(--slate)}
.post p{margin:14px 28px 0;font-size:11.5px;line-height:16px;color:var(--muted)}
.post .btn{left:28px;top:310px;width:88px;height:26px;font-size:10.5px;border-radius:4px}

/* footer */
.site-footer{position:absolute;left:0;top:3151px;width:1200px;height:644px;background:var(--footer);color:var(--white)}
.cta{position:absolute;left:132px;top:96px;width:934px;height:243px;border-radius:10px;overflow:hidden}
.cta-copy{position:absolute;left:626px;top:140px;width:440px}
.cta-copy h2{font-family:'Josefin Sans',sans-serif;font-weight:600;font-size:24px;line-height:29px;letter-spacing:.6px;color:var(--slate)}
.cta-copy p{margin-top:10px;width:380px;font-size:14.5px;line-height:18px;color:var(--white)}
.cta-copy .btn{position:static;margin-top:14px;width:126px;height:38px;font-size:14px}
.site-footer .brand{left:135px;top:420px;font-size:32px;color:var(--white)}
.site-footer .brand .dot{width:36px;height:36px;background:var(--slate)}
.f-head{position:absolute;top:387px;font-weight:800;font-size:13px;letter-spacing:.5px}
.f-contact{position:absolute;left:546px;display:flex;gap:10px;font-size:12px;line-height:16px}
.f-contact .ico{width:22px;height:22px;border-radius:50%;background:var(--white);margin-top:4px}
.f-menu{position:absolute;left:807px;top:425px;list-style:none;font-size:12px;line-height:20px}
.f-social{position:absolute;left:982px;top:414px;display:flex;gap:6px}
.f-social i{width:26px;height:26px;border-radius:50%;background:var(--white);display:block}
.f-line{position:absolute;left:132px;top:555px;width:934px;height:1px;background:#444}
.copy{position:absolute;left:0;top:592px;width:1200px;text-align:center;font-size:12px}
</style>
</head>
<body>
<svg width="0" height="0" style="position:absolute">
  <defs>
    <linearGradient id="g-office" x1="0" y1="0" x2="1" y2="1"><stop offset="0" stop-color="#c9d3d6"/><stop offset=".5" stop-color="#8aa0ae"/><stop offset="1" stop-color="#dfe4e6"/></linearGradient>
    <linearGradient id="g-meeting" x1="0" y1="0" x2="1" y2="1"><stop offset="0" stop-color="#e7ebee"/><stop offset=".55" stop-color="#5d6a78"/><stop offset="1" stop-color="#f1f2f3"/></linearGradient>
    <linearGradient id="g-city" x1="0" y1="0" x2="0" y2="1"><stop offset="0" stop-color="#a9b4c3"/><stop offset=".25" stop-color="#f0a352"/><stop offset=".55" stop-color="#6f7f95"/><stop offset="1" stop-color="#3d4a5a"/></linearGradient>
  </defs>
</svg>

<header class="site-header">
  <div class="brand"><span class="dot"></span>SME BRIGHTFOLD</div>
  <div class="abs follow">FOLLOW US <i></i><i></i><i></i></div>
  <div class="abs call">
    <span class="ico"><svg width="14" height="14" viewBox="0 0 24 24"><path fill="#fff" d="M6.6 10.8a15 15 0 0 0 6.6 6.6l2.2-2.2c.3-.3.7-.4 1-.2 1.1.4 2.3.6 3.6.6.6 0 1 .4 1 1V20c0 .6-.4 1-1 1A17 17 0 0 1 3 4c0-.6.4-1 1-1h3.5c.6 0 1 .4 1 1 0 1.3.2 2.5.6 3.6.1.3 0 .7-.2 1z"/></svg></span>
    <div><small>CALL US</small><strong>+1 555 014 2290</strong></div>
  </div>
  <nav class="abs nav"><span class="active">HOME</span><span>ABOUT US</span><span>SERVICES</span><span>BLOG</span><span>CONTACT US</span></nav>
</header>

<section class="hero">
  <h1>GET REAL ADVICE<br><span>FROM REAL PEOPLE</span></h1>
  <p>Lorem Ipsum is simply dummy text of the printing and typesetting industry.</p>
  <a class="btn" style="left:131px;top:304px;width:128px;height:38px;font-size:14px">READ MORE</a>
  <div class="abs" style="left:0;top:103px;width:1200px;height:492px;overflow:hidden">
    <div class="diamond" role="img" aria-label="Business partners shaking hands across a meeting table" style="left:245px;top:285px;width:170px;height:170px;background:linear-gradient(135deg,#dfe3e4,#6b7680 55%,#eef0f0)"></div>
    <div class="diamond" role="img" aria-label="Advisor meeting a client in a bright office" style="left:436px;top:200px;width:182px;height:182px;background:linear-gradient(135deg,#d9e2e5,#587589 55%,#e9edef)"></div>
  </div>
  <svg class="photo" style="left:607px;top:103px" width="460" height="462" viewBox="0 0 460 462" role="img" aria-label="Team of advisors discussing charts around a table">
    <path fill="url(#g-meeting)" d="M38,0 H420 Q462,0 456,42 L402,420 Q396,462 352,462 H108 Q64,462 58,420 L4,42 Q-2,0 38,0Z"/>
  </svg>
</section>

<section class="services">
  <div class="band-soft" style="top:595px;height:462px"></div>
  <h2 class="sec-title" style="top:633px">OUR <span>SERVICES</span></h2>
  <div class="rule" style="left:584px;top:675px"></div>

  <article class="service" style="left:132px">
    <svg width="56" height="50" viewBox="0 0 56 50" fill="none" stroke="#7a8899" stroke-width="3"><path d="M4 6h32v20H16l-8 7v-7H4z" fill="#7a8899"/><path d="M40 16h12v18h-4v6l-7-6H24v-4"/></svg>
    <h3>Business advisory service</h3>
    <p>There are many variations of passages of Lorem Ipsum avail able, but the majority have suffered alteration in.</p>
    <a class="btn">READ MORE</a>
  </article>
  <article class="service featured" style="left:371px">
    <svg width="56" height="50" viewBox="0 0 56 50" fill="none" stroke="#fff" stroke-width="2.5"><rect x="14" y="4" width="38" height="22" rx="2"/><circle cx="16" cy="24" r="6"/><path d="M6 48v-10l10-4 10 4v10"/><path d="M28 14l8-4 6 6"/></svg>
    <h3>Regional business support</h3>
    <p>There are many variations of passages of Lorem Ipsum avail able, but the majority have suffered alteration in.</p>
    <a class="btn">READ MORE</a>
  </article>
  <article class="service" style="left:607px">
    <svg width="56" height="50" viewBox="0 0 56 50" fill="none" stroke="#7a8899" stroke-width="2.5"><circle cx="28" cy="25" r="8"/><path d="M28 4v6M28 40v6M7 25h6M43 25h6M13 10l4 4M39 36l4 4M13 40l4-4M39 14l4-4"/><circle cx="28" cy="25" r="16"/></svg>
    <h3>Dispute resolution service</h3>
    <p>There are many variations of passages of Lorem Ipsum avail able, but the majority have suffered alteration in.</p>
    <a class="btn">READ MORE</a>
  </article>
  <article class="service" style="left:844px">
    <svg width="56" height="50" viewBox="0 0 56 50" fill="none" stroke="#7a8899" stroke-width="2.5"><circle cx="34" cy="18" r="12"/><path d="M29 18h2M34 18h1M38 18h1"/><path d="M10 18c-4 6 2 20 14 26 4 2 7 0 8-3l-5-5-4 2c-4-2-7-6-8-10l3-3-4-6z"/></svg>
    <h3>Support Businesses</h3>
    <p>There are many variations of passages of Lorem Ipsum avail able, but the majority have suffered alteration in.</p>
    <a class="btn">READ MORE</a>
  </article>
</section>

<section class="welcome">
  <svg class="photo" style="left:132px;top:1098px" width="460" height="460" viewBox="0 0 460 460" role="img" aria-label="Two colleagues reviewing work on a laptop">
    <path fill="url(#g-office)" d="M40,0 H418 Q462,0 456,44 L404,418 Q398,460 354,460 H106 Q62,460 56,418 L4,44 Q-2,0 40,0Z"/>
  </svg>
  <h2>WELCOME TO<br><span>SME BRIGHTFOLD</span></h2>
  <div class="rule" style="left:644px;top:1207px"></div>
  <p class="lead">Lorem Ipsum is simply dummy text of the printing and typesetting industry</p>
  <p class="body-copy" style="left:644px;top:1302px;width:415px">It is a long established fact that a reader will be distracted by the readable content of a page when looking at its layout. The point of using Lorem Ipsum is that it has a more-or-less normal distribution of letters, as opposed to using 'Content here, content here', making it look like readable English. Many desktop publishing packages Lorem Ipsum generators on the Internet tend to repeat predefined chunks as necessary making this the first true generator.</p>
  <a class="btn" style="left:644px;top:1487px;width:128px;height:40px;font-size:14px">READ MORE</a>
</section>

<section class="why">
  <h2 class="why-title">WHY SME BRIGHTFOLD</h2>
  <div class="rule"></div>
  <div class="reason" style="left:125px">
    <svg width="82" height="82" viewBox="0 0 82 82" fill="none" stroke="#fff" stroke-width="3"><path d="M14 30a28 28 0 0 1 48-12M68 52a28 28 0 0 1-48 12"/><path d="M62 8v10H52M20 74V64h10"/><circle cx="41" cy="36" r="11"/><path d="M36 48h10v8H36z"/></svg>
    <h3>Improve Efficiency</h3>
    <p>It is a long established fact that a reader will be distracted by the readable content of a page when looking at its layout. The point of using Lorem Ipsum is that it has a more-or-less normal distribution of letters, as opposed to using 'Content here, content here'</p>
  </div>
  <div class="reason" style="left:460px">
    <svg width="86" height="82" viewBox="0 0 86 82" fill="none" stroke="#fff" stroke-width="3"><circle cx="34" cy="18" r="13"/><path d="M6 74c0-20 12-32 28-32 6 0 11 2 15 5M6 74h34"/><circle cx="64" cy="60" r="8"/><path d="M64 44v6M64 70v6M48 60h6M74 60h6M53 49l4 4M71 67l4 4M53 71l4-4M71 53l4-4"/></svg>
    <h3>Manage Business Risk</h3>
    <p>It is a long established fact that a reader will be distracted by the readable content of a page when looking at its layout. The point of using Lorem Ipsum is that it has a more-or-less normal distribution of letters, as opposed to using 'Content here, content here'</p>
  </div>
  <div class="reason" style="left:793px">
    <svg width="82" height="82" viewBox="0 0 82 82" fill="none" stroke="#fff" stroke-width="3"><path d="M74 8C54 8 38 20 28 40l14 14c20-10 32-26 32-46z"/><circle cx="54" cy="28" r="6"/><path d="M30 38H18l-8 10h14M44 52v12l-10 8V58"/><path d="M22 58c-8 2-12 8-12 14 6 0 12-4 14-12"/></svg>
    <h3>Grow Your Business And Brand</h3>
    <p>It is a long established fact that a reader will be distracted by the readable content of a page when looking at its layout. The point of using Lorem Ipsum is that it has a more-or-less normal distribution of letters, as opposed to using 'Content here, content here'</p>
  </div>
</section>

<section class="skills">
  <h2>BUILD THE SKILLS<br><span>TO SUCCEED</span></h2>
  <div class="rule" style="left:132px;top:2233px"></div>
  <p class="body-copy" style="left:132px;top:2272px;width:412px;line-height:22.5px">It is a long established fact that a reader will be distracted by the readable content of a page when looking at its layout. The point of using Lorem Ipsum is that it has a more-or-less normal distribution of letters, as opposed to using 'Content here, content here', making it look like readable English. Many desktop publishing packages Lorem Ipsum generators on the Internet tend to repeat predefined chunks as necessary making this the first true generator.</p>
  <a class="btn" style="left:132px;top:2486px;width:128px;height:40px;font-size:14px">READ MORE</a>
  <svg class="photo" style="left:568px;top:2103px" width="498" height="462" viewBox="0 0 498 462" role="img" aria-label="Businessman climbing stairs toward a sunlit city skyline">
    <path fill="url(#g-city)" d="M40,0 H458 Q500,0 494,42 L442,420 Q436,462 392,462 H106 Q62,462 56,420 L4,42 Q-2,0 40,0Z"/>
  </svg>
</section>

<section class="blog">
  <div class="band-soft" style="top:2610px;height:541px"></div>
  <h2 class="sec-title" style="top:2654px">LATEST <span>BLOG</span></h2>
  <div class="rule" style="left:584px;top:2700px"></div>
  <article class="post" style="left:131px">
    <div class="photo" role="img" aria-label="Rising arrow over a growth bar chart" style="background:linear-gradient(135deg,#2a4468,#6f93b8 60%,#1c3150)"></div>
    <h3>There are many variations of passages of Lorem Ipsum</h3>
    <p>There are many variations of passages of Lorem Ipsum avail able, but the majority have suffered alteration in.</p>
    <a class="btn">READ MORE</a>
  </article>
  <article class="post" style="left:449px">
    <div class="photo" role="img" aria-label="Two smiling colleagues working at a laptop" style="background:linear-gradient(135deg,#c6c2b8,#6d7c8e 55%,#d9d5cc)"></div>
    <h3>It is a long established fact that a reader will be</h3>
    <p>There are many variations of passages of Lorem Ipsum avail able, but the majority have suffered alteration in.</p>
    <a class="btn">READ MORE</a>
  </article>
  <article class="post" style="left:767px">
    <div class="photo" role="img" aria-label="Shop owner holding a tablet in her store" style="background:linear-gradient(135deg,#8a6e55,#c8b39c 55%,#6b5644)"></div>
    <h3>There are many variations of passages of Lorem Ipsum</h3>
    <p>There are many variations of passages of Lorem Ipsum avail able, but the majority have suffered alteration in.</p>
    <a class="btn">READ MORE</a>
  </article>
</section>

<footer class="site-footer">
  <div class="cta" role="img" aria-label="Dim café interior in the background" style="background:linear-gradient(90deg,#4a4640,#2a2724 45%,#3a342c)"></div>
  <div class="abs" role="img" aria-label="Smiling small business owner in a yellow top and apron" style="left:331px;top:22px;width:287px;height:317px;border-radius:140px 140px 0 0;background:linear-gradient(180deg,#b88a6a,#e2b13c 55%,#c89a2e)"></div>
  <div class="cta-copy">
    <h2>Contrary to popular belief, Lorem<br>Ipsum is not simply random</h2>
    <p>There are many variations of passages of Lorem Ipsum available, but the majority have</p>
    <a class="btn">CONTACT US</a>
  </div>

  <div class="brand"><span class="dot"></span>SME BRIGHTFOLD</div>

  <h4 class="f-head" style="left:546px">CONTACT US</h4>
  <div class="f-contact" style="top:426px"><span class="ico"></span><div>Call Us<br>+1 555 014 2290</div></div>
  <div class="f-contact" style="top:478px"><span class="ico"></span><div>E mail Us<br>info@smebrightfold.com</div></div>

  <h4 class="f-head" style="left:807px">MENU</h4>
  <ul class="f-menu"><li>HOME</li><li>ABOUT US</li><li>SERVICES</li><li>BLOG</li><li>CONTACT US</li></ul>

  <h4 class="f-head" style="left:982px">FOLLOW US</h4>
  <div class="f-social"><i></i><i></i><i></i></div>

  <div class="f-line"></div>
  <p class="copy">Copyright © 2022 All Rights Reserved</p>
</footer>
</body>
</html>
```